Design the Business card for NetVaultix

Business card required for a professional Cyber Security business.
Company Logo and Icon has already been provided however I would like other options for the logo and icon to compare to. Alternatively, please refine/enhance the image of the logo.icon I have already provided.

If you are going to use the provided logo and icon, I was thinking that the company raised Logo on White background would serve well on the front of the card. See attached. AND, a large company raised stand-alone icon to appear on black background on the back of the card with tagline 'Cyber Risk Management, Governance and Consulting' or 'Cyber Security for your Business' See attached.
Alternatively, provide your own design for the logo and icon.

Target Market(s)

Enterprise, Government, Financial.

Contact Information for Business Card

Teodor Vaskelin
Founder and CEO

Email Address
Mobile Number
Website URL
LinkedIn URL

Logo Text

NetVaultix - see attached example of logo

Font styles to use
Other font styles liked:
• Berlin Sans FB

Requirements
Must have
• Clean large and bold icon on the back with tagline.
• Horizontal alignment,
Nice to have
• Round edges.
• Raised Logo/Icon
Should not have
• An unprofessional look and feel.

```html
<!DOCTYPE html>
<html lang="en">
<head>
<meta charset="utf-8">
<title>NetVaultix Business Card</title>
<link href="https://fonts.googleapis.com/css2?family=Open+Sans:wght@400;700&display=swap" rel="stylesheet">
<style>
  :root {
    --bg: #dcdcdc;
    --navy: #1d4a86;
    --steel: #7b7f88;
    --ink: #23262b;
    --card-white: #fbfbfb;
    --card-black: #1c1c1d;
    --tagline: #2d5a96;
  }
  * { margin: 0; padding: 0; box-sizing: border-box; }
  html, body { width: 1200px; height: 900px; overflow: hidden; }
  body {
    background: var(--bg);
    font-family: "Open Sans", Arial, sans-serif;
    position: relative;
  }
  .card {
    position: absolute;
    width: 500px;
    height: 286px;
    border-radius: 22px;
    box-shadow: 0 8px 22px rgba(0,0,0,0.22);
    overflow: hidden;
  }
  .card-front { left: 70px; top: 250px; background: var(--card-white); }
  .card-back  { left: 630px; top: 250px; background: var(--card-black); }

  .holder { position: absolute; left: 40px; top: 34px; }
  .holder-name { font-size: 24px; color: var(--steel); font-weight: 400; line-height: 1.1; }
  .holder-title { font-size: 13px; color: var(--navy); margin-top: 2px; }
  .rule { width: 62px; height: 3px; background: var(--navy); margin: 20px 0 16px; }
  .contacts { list-style: none; }
  .contacts li {
    display: flex; align-items: center; gap: 8px;
    font-size: 13px; color: var(--ink); margin-bottom: 7px;
  }
  .contacts svg { width: 13px; height: 13px; flex: none; }
  .website { font-size: 13px; color: var(--navy); }

  .front-brand {
    position: absolute; right: 36px; bottom: 46px;
    display: flex; align-items: center; gap: 10px;
  }
  .brand-square { width: 22px; height: 22px; background: var(--navy); }
  .brand-name {
    font-weight: 700; font-size: 30px; letter-spacing: 2px;
    color: var(--navy); text-transform: uppercase;
  }

  .back-brand {
    position: absolute; left: 0; right: 0; top: 92px;
    display: flex; justify-content: center; align-items: center; gap: 12px;
  }
  .back-brand .brand-square { background: var(--steel); width: 26px; height: 26px; }
  .back-brand .brand-name { color: var(--tagline); font-size: 36px; }
  .tagline {
    position: absolute; left: 0; right: 0; top: 176px;
    text-align: center; font-size: 14px; color: var(--tagline);
  }

  .showcase-brand {
    position: absolute; right: 70px; top: 700px;
    display: flex; align-items: center; gap: 12px;
  }
  .showcase-brand .brand-square { width: 30px; height: 30px; }
  .showcase-brand .brand-name { font-size: 40px; }
</style>
</head>
<body>
  <section class="card card-front" aria-label="Card front">
    <div class="holder">
      <p class="holder-name">Teodor Vaskelin</p>
      <p class="holder-title">Founder and CEO</p>
      <div class="rule"></div>
      <ul class="contacts">
        <li>
          <svg viewBox="0 0 16 16" aria-hidden="true"><path fill="#1d4a86" d="M2 5c0-2 2-3 6-3s6 1 6 3v1h-3V5H5v1H2zM4 7h8l2 7H2z"/><circle cx="8" cy="10.5" r="1.6" fill="#fbfbfb"/></svg>
          000 000 0000
        </li>
        <li>
          <svg viewBox="0 0 16 16" aria-hidden="true"><rect x="1" y="3" width="14" height="10" fill="#1d4a86"/><path d="M1 3l7 6 7-6" fill="none" stroke="#fbfbfb" stroke-width="1.3"/></svg>
          youremail@xyz.ocm
        </li>
        <li>
          <svg viewBox="0 0 16 16" aria-hidden="true"><rect x="1" y="1" width="14" height="14" rx="2" fill="#1d4a86"/></svg>
          /tvaskelin
        </li>
      </ul>
      <div class="rule"></div>
      <p class="website">www.netvaultix.com</p>
    </div>
    <div class="front-brand">
      <span class="brand-square"></span>
      <span class="brand-name">NetVaultix</span>
    </div>
  </section>

  <section class="card card-back" aria-label="Card back">
    <div class="back-brand">
      <span class="brand-square"></span>
      <span class="brand-name">NetVaultix</span>
    </div>
    <p class="tagline">Cyber Risk Management, Governance and Consulting</p>
  </section>

  <div class="showcase-brand">
    <span class="brand-square"></span>
    <span class="brand-name">NetVaultix</span>
  </div>
</body>
</html>
```